TWD OPRA Thank You card

We need a thank you card to give to our various stakeholders. The card design needs to be professional, corporate, and use elements of our current visual identity (colours and logo will be supplied). The inside of the card needs to have a space for a personal message to be written. Our target card size is 5 x 7.

As a bit of background, we fund local health care in Ontario. We do not directly provide front-line health care services. We do manage the funding and performance monitoring for the agencies we fund. We engage a wide range of people from CEO's, to MPP's, to the general public on a variety of health care topics. At the heart of it, we are a local organization that works to improve health care in Windsor/Essex, Chatham-Kent, and Sarnia/Lambton.

The final design should lean towards a more traditional look.

Industry/Entity Type

It Professional

Requirements
Must have
• It must incorporate our colour pallet and logo

```html
<!DOCTYPE html>
<html lang="en">
<head>
<meta charset="utf-8">
<title>Thank You Card</title>
<link rel="stylesheet" href="https://fonts.googleapis.com/css2?family=Pinyon+Script&display=swap">
<style>
  :root {
    --paper: #ffffff;
    --ink-grey: #8d8e91;
    --damask-tint: #f5f4ee;
    --band-grey: #96979b;
    --trim-gold: #d3bf8c;
    --scroll-silver: #dcdde0;
    --flourish-gold: #d7c38f;
  }
  html, body {
    margin: 0;
    padding: 0;
    overflow: hidden;
    background: var(--paper);
  }
  .card {
    position: relative;
    width: 1200px;
    height: 857px;
    overflow: hidden;
    background: var(--paper);
  }
  .damask-crest {
    position: absolute;
    left: 90px;
    top: 0;
    width: 1020px;
    height: 240px;
  }
  .greeting {
    position: absolute;
    left: -22px;
    width: 1200px;
    top: 313px;
    margin: 0;
    text-align: center;
    font-family: "Pinyon Script", cursive;
    font-weight: 400;
    font-size: 220px;
    line-height: 1;
    color: var(--ink-grey);
    letter-spacing: -2px;
    white-space: nowrap;
    z-index: 2;
  }
  .dotted-rule {
    position: absolute;
    left: 0;
    top: 480px;
    width: 1200px;
    height: 100px;
    z-index: 1;
  }
  .footer-band {
    position: absolute;
    left: 0;
    bottom: 0;
    width: 1200px;
    height: 150px;
    background: var(--band-grey);
    border-top: 7px solid var(--trim-gold);
    box-sizing: border-box;
  }
  .band-ornament {
    position: absolute;
    left: 0;
    top: 0;
    width: 1200px;
    height: 143px;
  }
</style>
</head>
<body>
  <main class="card">
    <svg class="damask-crest" viewBox="0 0 1020 240" role="img" aria-label="Faint cream damask ornament crest">
      <defs>
        <radialGradient id="crestFade" cx="50%" cy="25%" r="55%">
          <stop offset="0%" stop-color="var(--damask-tint)" stop-opacity="1"/>
          <stop offset="60%" stop-color="var(--damask-tint)" stop-opacity="0.8"/>
          <stop offset="100%" stop-color="var(--damask-tint)" stop-opacity="0"/>
        </radialGradient>
      </defs>
      <rect x="0" y="0" width="1020" height="240" fill="url(#crestFade)"/>
    </svg>

    <h1 class="greeting">Thank you</h1>

    <svg class="dotted-rule" viewBox="0 0 1200 100" aria-hidden="true">
      <path d="M84 57 Q300 78 560 62 T1116 34" fill="none" stroke="var(--ink-grey)" stroke-width="5" stroke-linecap="round" stroke-dasharray="0 13"/>
    </svg>

    <footer class="footer-band">
      <svg class="band-ornament" viewBox="0 0 1200 143" preserveAspectRatio="none" role="img" aria-label="Silver scrollwork with a central gold acanthus flourish">
        <defs>
          <linearGradient id="bandFlourish" x1="0" y1="0" x2="1" y2="0">
            <stop offset="0%" stop-color="var(--scroll-silver)"/>
            <stop offset="22%" stop-color="var(--band-grey)"/>
            <stop offset="38%" stop-color="var(--band-grey)"/>
            <stop offset="50%" stop-color="var(--flourish-gold)"/>
            <stop offset="62%" stop-color="var(--band-grey)"/>
            <stop offset="78%" stop-color="var(--band-grey)"/>
            <stop offset="100%" stop-color="var(--scroll-silver)"/>
          </linearGradient>
        </defs>
        <rect x="0" y="0" width="1200" height="143" fill="url(#bandFlourish)"/>
      </svg>
    </footer>
  </main>
</body>
</html>
```